Neuroepigenetics Symposium Save the Date

We need a Save the Date flyer for our upcoming Neuroepigenetics Symposium. This flyer should include the following:

Speakers, which we have eleven speakers with two name lecture speakers for this event.

1. Quimby Lecture:
Lorna Pettavel, M.D.
Professor in the departments of Pediatrics, Molecular and Human Genetics, and Neurology and Neuroscience at Ferncastle College of Medicine, the director of the Rita and Hal Ostrander Neurological Research Institute at Greyfield Children’s Hospital, and an investigator of the Calloway Pike Medical Institute.
2. Tindall Lecture:
Patrick Vallenford, Ph.D.
Oswin Thale Brightmore Professor of Neurobiology at Ellsworth Medical School
3. R. Simon Garrow, Ph.D.
Professor and Chairman, Department of Pharmacology at Kestrelmoor University.
4. Teodor Lusk, M.D., Ph.D.
Hartwell Professor and Chair of Neuroscience at Ashgrove University Tremont
5. Clara Voight, Ph.D.
Associate Professor of Neuroscience and Psychiatry at Barrowby School of Medicine at Elm Ridge
6. Tomas Vrbenko, Ph.D.
Associate Professor of Pathology, Neurology & Neuroscience at Halberd University
7. Meiling Kuang, Ph.D.
Associate Professor of Genetics at the Whitcombe School of Medicine at the University of Corvale
8. Margaret Dunstan, Ph.D.
Assistant Professor of Pharmacology at the Whitcombe School of Medicine at the University of Corvale
9. Federico Maltese, Ph.D.
Assistant Professor of Cell and Developmental Biology at the Whitcombe School of Medicine at the University of Corvale
10. Rebecca Tolland-Marsh, Ph.D.
Assistant Professor of Bioengineering at the School of Engineering and Applied Science at the University of Corvale
11. Gloria Festari, Ph.D.
Winifred T.L. Oakes Professor of Biology; Investigator of the Calloway Pike Medical Institute at the School of Arts and Sciences at the University of Corvale.
***Please shorten if necessary.

Date/Time, this event will take place on January 9th, 2017 from 8:30am - 6pm with reception from 5-6pm, and on January 10th, 2017 from 8:30am - 12pm.

Location, is Brackett Center for Translational Research, Hollister Auditorium and Lobby, 2716 Larkfield Park Blvd, Philadelphia, PA 19187.

Title of event, QIBR 33rd Annual Symposium "Year of Neuroepigenetics". This symposium is a joint collaboration sponsors by the Corvale Epigenetics Program, and Thornbury Institute for Neurosciences (QIBR). (department logos attached)

Outside sponsor, Helixmora's logo can be really small on the flyer. (logo attached)

I hope to include pictures of the speakers, but I am still waiting for them to send me the images they would like me to use. So, please work with this for now.

```html
<!DOCTYPE html>
<html lang="en">
<head>
<meta charset="utf-8">
<title>QIBR 33rd Annual Symposium — Year of Neuroepigenetics</title>
<link rel="stylesheet" href="https://fonts.googleapis.com/css2?family=Montserrat:wght@400;600;700&family=Source+Sans+3:wght@700;800&display=swap">
<style>
  :root {
    --backdrop: #5a5a5a;
    --paper: #ffffff;
    --brand-red: #b5343a;
    --brand-blue: #2b5797;
    --ring-blue: #2e6aa8;
    --ink: #1c1c1c;
    --placeholder-top: #d9d9d9;
    --placeholder-bottom: #b9b9b9;
  }
  * { margin: 0; padding: 0; box-sizing: border-box; }
  html, body { width: 1200px; height: 1200px; overflow: hidden; }
  body {
    background: var(--backdrop);
    font-family: "Montserrat", Arial, sans-serif;
    color: var(--ink);
  }
  .flyer {
    position: absolute;
    left: 153px; top: 22px;
    width: 893px; height: 1155px;
    background: var(--paper);
    overflow: hidden;
  }
  .band-top { position: absolute; left: 0; top: 0; width: 100%; height: 17px; background: var(--brand-red); }
  .band-bottom { position: absolute; left: 0; bottom: 0; width: 100%; height: 32px; background: var(--brand-blue); }

  .event-title {
    position: absolute; left: 0; top: 40px; width: 100%;
    text-align: center;
    font-family: "Source Sans 3", Arial, sans-serif;
    font-weight: 800;
    font-size: 51px; line-height: 52px;
    color: var(--brand-blue);
    text-shadow: 2px 3px 4px rgba(0,0,0,0.25);
    letter-spacing: 0.3px;
  }

  .hero-art {
    position: absolute; left: 40px; top: 167px;
    width: 103px; height: 128px; border-radius: 8px;
    background: linear-gradient(135deg, #8e2a44 0%, #5e4a66 50%, #3b5478 100%);
  }

  .schedule { position: absolute; left: 165px; top: 164px; width: 460px; }
  .schedule .date {
    color: var(--brand-red); font-weight: 700; font-size: 19.5px; line-height: 24px;
  }
  .schedule .date sup { font-size: 11px; }
  .schedule .note { font-size: 15px; line-height: 20px; margin-bottom: 4px; }
  .schedule .venue { font-size: 14.5px; font-weight: 600; line-height: 20.5px; margin-top: 3px; }

  .program-mark {
    position: absolute; left: 640px; top: 200px; width: 220px;
    display: flex; align-items: center; gap: 8px;
    font-weight: 700; font-size: 15px; line-height: 19px; color: var(--brand-blue);
  }
  .program-mark .dot { flex: none; width: 42px; height: 42px; border-radius: 50%; background: var(--brand-blue); }
  .sponsor-mark {
    position: absolute; left: 712px; top: 300px;
    font-weight: 700; font-size: 13px; color: #2a2a2a; letter-spacing: 1px;
  }

  .speaker { position: absolute; }
  .portrait {
    position: absolute; width: 114px; height: 114px; border-radius: 50%;
    border: 4px solid var(--ring-blue);
    background: linear-gradient(180deg, var(--placeholder-top), var(--placeholder-bottom));
  }
  .portrait.photo { background: linear-gradient(160deg, #5f7f52, #3b4a63); }
  .speaker .lecture {
    font-weight: 700; font-size: 11.5px; letter-spacing: 0.8px;
    color: var(--brand-red); margin-bottom: 3px;
  }
  .speaker h3 { font-weight: 700; font-size: 14.5px; letter-spacing: 0.3px; margin-bottom: 6px; }
  .speaker p { font-size: 13px; line-height: 17.5px; }
  .speaker.left { left: 165px; width: 420px; }
  .speaker.left.wide { width: 590px; }
  .speaker.right { right: 168px; width: 280px; text-align: right; }
</style>
</head>
<body>
<main class="flyer">
  <div class="band-top"></div>

  <h1 class="event-title">QIBR 33RD ANNUAL SYMPOSIUM<br>"YEAR OF NEUROEPIGENETICS"</h1>

  <div class="hero-art" role="img" aria-label="Illustration of a brain in red and blue belongs here"></div>

  <section class="schedule">
    <p class="date">JANUARY 9<sup>TH</sup>, 2017 FROM 8:30AM - 6PM</p>
    <p class="note">(with reception from 5-6pm)</p>
    <p class="date">JANUARY 10<sup>TH</sup>, 2017 FROM 8:30AM - 12PM.</p>
    <p class="venue">Location, is Brackett Center for Translational Research, Hollister Auditorium and Lobby, 2716 Larkfield Park Blvd, Philadelphia, PA 19187.</p>
  </section>

  <div class="program-mark"><span class="dot"></span><span>Corvale Epigenetics Program</span></div>
  <div class="sponsor-mark">HELIXMORA</div>

  <div class="portrait" style="left:35px;top:333px" role="img" aria-label="Speaker portrait to come"></div>
  <article class="speaker left wide" style="top:331px">
    <p class="lecture">QUIMBY LECTURE</p>
    <h3>LORNA PETTAVEL, M.D.</h3>
    <p>Professor in the departments of Pediatrics, Molecular and Human Genetics, and Neurology and Neuroscience at Ferncastle College of Medicine, the director of the Rita and Hal Ostrander Neurological Research Institute at Greyfield Children’s Hospital, and an investigator of the Calloway Pike Medical Institute.</p>
  </article>

  <div class="portrait" style="left:35px;top:463px" role="img" aria-label="Speaker portrait to come"></div>
  <article class="speaker left" style="top:474px">
    <p class="lecture">TINDALL LECTURE</p>
    <h3>PATRICK VALLENFORD, PH.D.</h3>
    <p>Oswin Thale Brightmore Professor of<br>Neurobiology at Ellsworth Medical School</p>
  </article>

  <div class="portrait photo" style="left:740px;top:463px" role="img" aria-label="Speaker photograph"></div>
  <article class="speaker right" style="top:488px">
    <h3>MEILING KUANG, PH.D.</h3>
    <p>Associate Professor of Genetics at the Whitcombe School of Medicine at the University of Corvale</p>
  </article>

  <div class="portrait" style="left:35px;top:588px" role="img" aria-label="Speaker portrait to come"></div>
  <article class="speaker left" style="top:614px;width:270px">
    <h3>R. SIMON GARROW, PH.D.</h3>
    <p>Professor and Chairman, Department of Pharmacology at Kestrelmoor University.</p>
  </article>

  <div class="portrait" style="left:740px;top:588px" role="img" aria-label="Speaker portrait to come"></div>
  <article class="speaker right" style="top:614px">
    <h3>MARGARET DUNSTAN, PH.D.</h3>
    <p>Assistant Professor of Pharmacology at the Whitcombe School of Medicine at the University of Corvale</p>
  </article>

  <div class="portrait" style="left:35px;top:718px" role="img" aria-label="Speaker portrait to come"></div>
  <article class="speaker left" style="top:731px;width:260px">
    <h3>TEODOR LUSK, M.D., PH.D.</h3>
    <p>Hartwell Professor and Chair of Neuroscience at Ashgrove University Tremont</p>
  </article>

  <div class="portrait" style="left:740px;top:718px" role="img" aria-label="Speaker portrait to come"></div>
  <article class="speaker right" style="top:731px;width:265px">
    <h3>FEDERICO MALTESE, PH.D.</h3>
    <p>Assistant Professor of Cell and Developmental Biology at the Whitcombe School of Medicine at the University of Corvale</p>
  </article>

  <div class="portrait" style="left:35px;top:846px" role="img" aria-label="Speaker portrait to come"></div>
  <article class="speaker left" style="top:870px;width:245px">
    <h3>CLARA VOIGHT, PH.D.</h3>
    <p>Associate Professor of Neuroscience and Psychiatry at Barrowby School of Medicine at Elm Ridge</p>
  </article>

  <div class="portrait" style="left:740px;top:846px" role="img" aria-label="Speaker portrait to come"></div>
  <article class="speaker right" style="top:870px;width:290px">
    <h3>REBECCA TOLLAND-MARSH, PH.D.</h3>
    <p>Assistant Professor of Bioengineering at the School of Engineering and Applied Science at the University of Corvale</p>
  </article>

  <div class="portrait" style="left:35px;top:975px" role="img" aria-label="Speaker portrait to come"></div>
  <article class="speaker left" style="top:998px;width:230px">
    <h3>TOMAS VRBENKO, PH.D.</h3>
    <p>Associate Professor of Pathology, Neurology &amp; Neuroscience at Halberd University</p>
  </article>

  <div class="portrait" style="left:740px;top:975px" role="img" aria-label="Speaker portrait to come"></div>
  <article class="speaker right" style="top:1000px;width:285px">
    <h3>GLORIA FESTARI, PH.D.</h3>
    <p>Winifred T.L. Oakes Professor of Biology; Investigator of the Calloway Pike Medical Institute at the School of Arts and Sciences at the University of Corvale.</p>
  </article>

  <div class="band-bottom"></div>
</main>
</body>
</html>
```